New Logo and Business Card

Want new logo and business card for multi brand website. Attached are the logos for the back of the card.
We want a new logo for the front, the name "Tallvisto" as the company name.
The logo can just be an "O" and a "B" for simplicity. With the text "Tallvisto" after it.
For the business card use this info:
Dale Furnow, PEng MBA
President
dale.furnow@tallvisto.ca
+14035512839
Industry/Entity Type
Business
Logo Text
Tallvisto
Logo styles of interest
Lettermark Logo

```html
<!DOCTYPE html>
<html lang="en">
<head>
<meta charset="utf-8">
<title>Tallvisto Business Card</title>
<link rel="stylesheet" href="https://fonts.googleapis.com/css2?family=Nunito:wght@300;400;800&display=swap">
<style>
  :root {
    --stage: #1c1c1e;
    --card-white: #f4f4f2;
    --ink: #1f1f1f;
    --teal: #1a98b3;
    --blue-light: #1b82c9;
    --blue-dark: #0a559a;
    --white: #ffffff;
  }
  * { box-sizing: border-box; margin: 0; padding: 0; }
  html, body {
    width: 1200px; height: 960px; overflow: hidden;
    background: var(--stage);
    font-family: "Nunito", sans-serif;
  }
  .canvas { position: relative; width: 1200px; height: 960px; }

  .card {
    position: absolute; left: 320px;
    width: 560px; height: 320px;
    border-radius: 3px;
    box-shadow: 0 10px 30px rgba(0,0,0,.55);
  }

  /* Front */
  .card-front { top: 110px; background: var(--card-white); color: var(--ink); }
  .brand {
    position: absolute; top: 34px; left: 0; right: 0;
    display: flex; flex-direction: column; align-items: center; gap: 8px;
  }
  .brand-square {
    width: 104px; height: 104px; background: var(--teal);
    border: 4px solid #fff; outline: 3px solid var(--teal);
  }
  .brand-name {
    font-weight: 800; font-size: 17px; letter-spacing: .5px;
    text-transform: uppercase; color: var(--ink);
  }
  .holder {
    position: absolute; top: 186px; left: 0; right: 0; text-align: center;
  }
  .holder-name { font-size: 24px; font-weight: 400; letter-spacing: .5px; line-height: 1.2; }
  .holder-creds { font-size: 13px; font-style: italic; font-weight: 300; letter-spacing: 0; }
  .holder-title { font-size: 14px; margin-top: 4px; }
  .contact {
    position: absolute; display: flex; align-items: center; gap: 5px;
    font-size: 16px; font-weight: 300; white-space: nowrap;
  }
  .contact svg { width: 16px; height: 16px; flex: none; }
  .contact-phone { top: 220px; right: 22px; }
  .contact-email { bottom: 20px; left: 22px; }

  /* Back */
  .card-back {
    top: 530px;
    background: radial-gradient(ellipse at 50% 40%, var(--blue-light), var(--blue-dark) 85%);
    display: flex; align-items: center; justify-content: center;
  }
  .back-name {
    color: var(--white); font-weight: 400; font-size: 44px;
    letter-spacing: 1px; text-transform: uppercase;
  }
</style>
</head>
<body>
<main class="canvas">
  <section class="card card-front">
    <div class="brand">
      <div class="brand-square"></div>
      <div class="brand-name">Tallvisto</div>
    </div>
    <div class="holder">
      <div class="holder-name">Dale Furnow, <span class="holder-creds">PEng MBA</span></div>
      <div class="holder-title">president</div>
    </div>
    <div class="contact contact-phone">
      <svg viewBox="0 0 24 24" aria-hidden="true"><path d="M6.6 10.8a15 15 0 0 0 6.6 6.6l2.2-2.2a1 1 0 0 1 1-.25 11.4 11.4 0 0 0 3.6.57 1 1 0 0 1 1 1V20a1 1 0 0 1-1 1A17 17 0 0 1 3 4a1 1 0 0 1 1-1h3.5a1 1 0 0 1 1 1c0 1.25.2 2.45.57 3.57a1 1 0 0 1-.25 1z" fill="none" stroke="var(--teal)" stroke-width="1.6"/></svg>
      <span>+14035512839</span>
    </div>
    <div class="contact contact-email">
      <svg viewBox="0 0 24 24" aria-hidden="true"><circle cx="12" cy="12" r="3.8" fill="none" stroke="var(--teal)" stroke-width="2"/><path d="M15.8 12v1.6a2.6 2.6 0 0 0 5.2 0V12a9 9 0 1 0-3.6 7.2" fill="none" stroke="var(--teal)" stroke-width="2"/></svg>
      <span>dale.furnow@tallvisto.ca</span>
    </div>
  </section>

  <section class="card card-back">
    <div class="back-name">Gleamwell Kits</div>
  </section>
</main>
</body>
</html>
```